Package design for quilted mattress covers.

We are producing a comfortable "quilted mattress protector" for beds . We need a very elegant and attractive and cozy insert label. approx. size is 14 inches high x11 inches wide. (One base design with slight edits to customize for each different bed size) It will be packaged in a nice clear bag, with the design label in front. I attached the type of product for reference

package text:
QUILTED MATTRESS COVER

size: 33x75x10"

*ultimate comfort
*breathable cotton top
*waterproof lining
*easy care wash and dry
Updates

Target Market(s)

displayed in drygood and bedding retail stores

Colors

Designer to choose colors to be used in the design.

Requirements
Must have
• all info as in description
Nice to have
• an image of a quilted cover on a bed, professionally included in the package design
Should not have
• ..

```html
<!DOCTYPE html>
<html lang="en">
<head>
<meta charset="utf-8">
<title>Velmora Quilted Mattress Cover – Insert Label</title>
<link href="https://fonts.googleapis.com/css2?family=Arimo:wght@400;700&family=Great+Vibes&family=Roboto:wght@300&display=swap" rel="stylesheet">
<style>
  :root {
    --brand-blue: #3d5a92;
    --script-blue: #3d5fa8;
    --band-blue: #6f8fd0;
    --light-blue: #8fb0e0;
    --panel-grey: #a7a8ab;
    --title-grey: #8a8a8c;
    --white: #ffffff;
  }
  * { margin: 0; padding: 0; box-sizing: border-box; }
  html, body { width: 944px; height: 1200px; overflow: hidden; background: var(--white); }
  .label { position: relative; width: 944px; height: 1200px; overflow: hidden; font-family: "Arimo", Arial, sans-serif; }

  .hero-photo {
    position: absolute; left: 0; top: 0; width: 944px; height: 938px;
    background:
      radial-gradient(ellipse 260px 110px at 700px 520px, rgba(255,255,255,.95) 0%, rgba(255,255,255,0) 75%),
      radial-gradient(ellipse 170px 150px at 640px 360px, #f2c9b4 0%, rgba(240,198,176,.85) 45%, rgba(240,198,176,0) 80%),
      radial-gradient(ellipse 150px 95px at 430px 320px, #f0d2bf 0%, rgba(240,210,191,0) 80%),
      radial-gradient(ellipse 330px 170px at 560px 330px, rgba(222,182,128,.85) 0%, rgba(222,182,128,.5) 45%, rgba(222,182,128,0) 78%),
      radial-gradient(ellipse 300px 120px at 150px 300px, #ffffff 0%, rgba(255,255,255,.85) 55%, rgba(255,255,255,0) 85%),
      radial-gradient(ellipse 420px 170px at 760px 590px, #ffffff 0%, rgba(250,250,252,.9) 50%, rgba(250,250,252,0) 85%),
      linear-gradient(180deg, #efe6dc 0%, #f3ede6 30%, #f1eeec 60%, #eceef2 100%);
  }
  .chevron { position: absolute; left: 0; top: 0; }
  .mattress-photo { position: absolute; left: 0; top: 0; }

  .tagline { position: absolute; font-family: "Great Vibes", cursive; color: var(--script-blue); line-height: 1; }
  .tagline--sleep { left: 181px; top: 62px; font-size: 78px; }
  .tagline--affirm { left: 70px; top: 146px; font-size: 82px; }

  .brand-name {
    position: absolute; left: 264px; top: 654px; transform: translate(-50%, -50%);
    display: flex; align-items: center; gap: 12px;
    font-weight: 700; font-size: 72px; letter-spacing: -3px; color: var(--brand-blue);
  }
  .brand-name__mark { width: 18px; height: 18px; background: var(--brand-blue); }

  .product-title { position: absolute; font-family: "Roboto", Arial, sans-serif; font-weight: 300; color: var(--title-grey); line-height: 1; }
  .product-title--line1 { left: 156px; top: 758px; font-size: 62px; letter-spacing: 1px; }
  .product-title--line2 { left: 42px; top: 822px; font-size: 62px; letter-spacing: 1.5px; }

  .size-banner { position: absolute; left: 0; top: 0; }
  .size-banner__text { position: absolute; right: 27px; top: 894px; color: var(--white); font-size: 28px; }

  .features { position: absolute; left: 0; top: 938px; width: 944px; height: 180px; background: var(--panel-grey); }
  .feature { position: absolute; display: flex; align-items: center; gap: 20px; color: var(--white); font-size: 18px; line-height: 23px; }
  .feature svg { width: 48px; height: 52px; flex: none; }
  .feature--comfort { left: 62px; top: 22px; }
  .feature--cotton { left: 60px; top: 104px; }
  .feature--cotton svg { width: 52px; }
  .feature--cotton { gap: 18px; }
  .feature--waterproof { left: 308px; top: 22px; }
  .feature--care { left: 310px; top: 104px; }

  .promise { position: absolute; left: 568px; top: 24px; width: 346px; color: var(--white); }
  .promise__title { font-weight: 700; font-size: 21px; line-height: 27px; padding-bottom: 9px; border-bottom: 1px solid rgba(255,255,255,.85); }
  .promise__text { margin-top: 11px; font-size: 12.6px; line-height: 17.8px; }

  .footer { position: absolute; left: 0; top: 1118px; width: 944px; height: 82px; background: var(--brand-blue); border-top: 2px solid var(--white); color: var(--light-blue); }
  .footer__maker { position: absolute; left: 57px; top: 8px; font-size: 9px; }
  .footer__name { position: absolute; left: 57px; top: 24px; font-size: 16px; }
  .footer__address { position: absolute; left: 57px; top: 42px; font-size: 11px; line-height: 15px; }
  .footer__contact { position: absolute; left: 312px; top: 38px; font-size: 11px; line-height: 16px; }
  .footer__web { position: absolute; left: 568px; top: 18px; color: var(--white); }
  .footer__web-lead { font-size: 16px; }
  .footer__web-url { margin-top: 8px; font-weight: 700; font-size: 20px; }
</style>
</head>
<body>
<div class="label">
  <div class="hero-photo" role="img" aria-label="Photo of a woman sleeping peacefully on a soft white pillow in a bright, warm bedroom"></div>

  <svg class="chevron" width="944" height="938" viewBox="0 0 944 938" aria-hidden="true">
    <polygon points="0,562 264,423 944,777 944,938 0,938" fill="var(--band-blue)" opacity=".28"/>
    <polygon points="0,586 264,447 944,801 944,938 0,938" fill="var(--band-blue)" opacity=".3"/>
    <polygon points="0,616 264,477 944,831 944,938 0,938" fill="var(--band-blue)" opacity=".35"/>
    <polygon points="0,640 264,501 944,855 944,938 0,938" fill="var(--white)"/>
    <polyline points="0,640 264,501 669,713" fill="none" stroke="var(--brand-blue)" stroke-width="2"/>
  </svg>

  <svg class="mattress-photo" width="944" height="938" viewBox="0 0 944 938" role="img" aria-label="Photo of a white quilted mattress cover with soft diamond stitching">
    <defs>
      <linearGradient id="mattressTop" x1="0" y1="0" x2="0.3" y2="1">
        <stop offset="0" stop-color="#ffffff"/>
        <stop offset=".6" stop-color="#f1f2f4"/>
        <stop offset="1" stop-color="#e2e4e8"/>
      </linearGradient>
      <linearGradient id="mattressSide" x1="0" y1="0" x2="0" y2="1">
        <stop offset="0" stop-color="#eceef1"/>
        <stop offset="1" stop-color="#d6d9de"/>
      </linearGradient>
    </defs>
    <path d="M600,800 Q600,770 630,756 L944,640 L944,882 L640,882 Q600,880 600,850 Z" fill="url(#mattressSide)"/>
    <path d="M606,776 Q612,752 640,742 L944,640 L944,800 L640,810 Q610,806 606,776 Z" fill="url(#mattressTop)"/>
  </svg>

  <div class="tagline tagline--sleep">Sleep</div>
  <div class="tagline tagline--affirm">Affirmations !</div>

  <div class="brand-name"><span class="brand-name__mark"></span>Velmora</div>

  <div class="product-title product-title--line1">Quilted</div>
  <div class="product-title product-title--line2">Mattress Cover</div>

  <svg class="size-banner" width="944" height="938" viewBox="0 0 944 938" aria-hidden="true">
    <polygon points="639,882 944,882 944,938 604,938" fill="var(--brand-blue)"/>
  </svg>
  <div class="size-banner__text">Size: 33 x 75 x 10"</div>

  <section class="features">
    <div class="feature feature--comfort">
      <svg viewBox="0 0 48 52" fill="none" stroke="#1d2a44" stroke-width="2"><rect x="5" y="3" width="38" height="46" rx="3" fill="var(--light-blue)"/><circle cx="24" cy="16" r="7" fill="#fff"/><path d="M9 26h30v20H9z" fill="#cfe0f7"/></svg>
      <span>Ultimate<br>Comfort</span>
    </div>
    <div class="feature feature--cotton">
      <svg viewBox="0 0 52 52" fill="none" stroke="#1d2a44" stroke-width="2"><circle cx="20" cy="10" r="6" fill="#fff"/><rect x="4" y="22" width="44" height="18" rx="4" fill="var(--light-blue)"/><path d="M8 40v6M44 40v6"/></svg>
      <span>Breathable<br>Cotton Top</span>
    </div>
    <div class="feature feature--waterproof">
      <svg viewBox="0 0 52 52" fill="none" stroke="#1d2a44" stroke-width="2"><path d="M34 4c6 8 9 12 9 16a9 9 0 0 1-18 0c0-4 3-8 9-16z" fill="var(--light-blue)"/><path d="M12 10c3 4 5 6 5 8a5 5 0 0 1-10 0c0-2 2-4 5-8z" fill="var(--light-blue)"/><path d="M4 32h44v10H4zM4 26v22M48 42v6"/></svg>
      <span>Waterproof<br>Lining</span>
    </div>
    <div class="feature feature--care">
      <svg viewBox="0 0 48 52" fill="none" stroke="#1d2a44" stroke-width="2"><rect x="5" y="3" width="38" height="46" rx="2" fill="#fff"/><path d="M5 12h38"/><circle cx="24" cy="30" r="11" fill="var(--light-blue)"/><circle cx="24" cy="30" r="5" fill="#fff"/></svg>
      <span>Easy Care<br>Wash &amp; Dry</span>
    </div>

    <div class="promise">
      <h2 class="promise__title">Total Protection<br>with Complete Comfort</h2>
      <p class="promise__text">The “Velmora” Quilted Mattress Cover<br>has been designed with advanced technology.<br>Quilted cover and generous ultra fine filling provide<br>improved comfort and extra protection for your mattress.</p>
    </div>
  </section>

  <footer class="footer">
    <div class="footer__maker">A Premium product by</div>
    <div class="footer__name">Velmora</div>
    <div class="footer__address">Company Addrss will be here.<br>Country.</div>
    <div class="footer__contact">Ph: +000 000 0000<br>E-Mail: info@velmoramail.com</div>
    <div class="footer__web">
      <div class="footer__web-lead">For More Products, visit us on</div>
      <div class="footer__web-url">www.velmora.com</div>
    </div>
  </footer>
</div>
</body>
</html>
```